Breast Cancer Stickers

Hi,
i would like a of small design for a breast cancer awareness campaign. please check attached picture this is the size and font i want. these will be stickers. Then i would like a little pink ribbon after each dot. so there will be four design please find below colors, slogans, etc..
1 I RISE I WIN. (Off white Background, Light Pink Font)
Never give up.
2 BOLD SPIRIT. (Black Background, Bright Pink Font)
Theres Always hope
3 HOPEFULLY BRAVE. ( Light Pink Background, Off white Font)
Stay Positive
4 LIGHT UP THE HOPE. (Bright Pink Background, Black font)
fight on.
Campaign

```html
<!DOCTYPE html>
<html lang="en">
<head>
<meta charset="utf-8">
<title>Awareness Stickers</title>
<link rel="stylesheet" href="https://fonts.googleapis.com/css2?family=Arimo:wght@700&display=swap">
<style>
  :root {
    --backdrop-light: #dcdcdc;
    --backdrop-dark: #b4b4b4;
    --off-white: #ffffff;
    --light-pink: #ff9fc9;
    --bright-pink: #ff1f6b;
    --black: #000000;
  }
  html, body {
    margin: 0;
    padding: 0;
    width: 1200px;
    height: 1000px;
    overflow: hidden;
  }
  body {
    position: relative;
    background: radial-gradient(ellipse at 50% 45%, var(--backdrop-light) 35%, var(--backdrop-dark) 100%);
    font-family: "Arimo", "Helvetica Neue", Arial, sans-serif;
    font-weight: 700;
  }
  .sticker {
    position: absolute;
    top: 375px;
    width: 250px;
    height: 250px;
    box-sizing: border-box;
  }
  .sticker--rise { left: 69px; background: var(--off-white); color: var(--light-pink); }
  .sticker--spirit { left: 340px; background: var(--black); color: var(--bright-pink); }
  .sticker--brave { left: 612px; background: var(--light-pink); color: var(--off-white); }
  .sticker--light-up { left: 883px; background: var(--bright-pink); color: var(--black); }

  .sticker__text {
    position: absolute;
    top: 88px;
  }
  .sticker--rise .sticker__text { left: 39px; }
  .sticker--spirit .sticker__text { left: 38px; }
  .sticker--brave .sticker__text { left: 25px; }
  .sticker--light-up .sticker__text { left: 28px; }

  .slogan {
    margin: 0;
    font-size: 35px;
    line-height: 33px;
    white-space: nowrap;
  }
  .tagline {
    margin: 3px 0 0;
    font-size: 17px;
    line-height: 20px;
    white-space: nowrap;
  }
  .dot {
    display: inline-block;
    width: 6px;
    height: 6px;
    margin-left: 3px;
    border-radius: 50%;
    background: currentColor;
    vertical-align: -2px;
  }
</style>
</head>
<body>

<section class="sticker sticker--rise">
  <div class="sticker__text">
    <h2 class="slogan">I RISE<br>I WIN<span class="dot"></span></h2>
    <p class="tagline">Never Give Up</p>
  </div>
</section>

<section class="sticker sticker--spirit">
  <div class="sticker__text">
    <h2 class="slogan">BOLD<br>SPIRIT<span class="dot"></span></h2>
    <p class="tagline">Theres Always Hope</p>
  </div>
</section>

<section class="sticker sticker--brave">
  <div class="sticker__text">
    <h2 class="slogan">HOPEFULLY<br>BRAVE<span class="dot"></span></h2>
    <p class="tagline">Stay Positive</p>
  </div>
</section>

<section class="sticker sticker--light-up">
  <div class="sticker__text">
    <h2 class="slogan">LIGHT UP<br>THE HOPE<span class="dot"></span></h2>
    <p class="tagline">Fight On</p>
  </div>
</section>

</body>
</html>
```